Agency Website & Personal brand

My name is Petros Valtinos & I've been a digital marketer & an e-commerce expert since 2010.

- I've spoken to 20 different events around the world up to 3,000 people in size.
- I've sold over 1500 training courses around e-commerce growth.
- I have over 100 testimonials (video & photo) from successful students who bought my training
- I have dozens of video testimonials from respected entrepreneurs that vouch for me and my work
- I have photos with marketing legends with that I shared the stage like Owen Farrow, Thomas Brennigan, Colin Marsh & more
- I am the host of the Aegean Roundtable since 2017 - a high-level networking event for 7 & 8 figure entrepreneurs - 100 people have come to Greece since 2017
- I have tons of videos created where I showcase my expertise on growth
- I have worked with dozens of e-commerce stores on their growth & helped them scale to multiple 6, 7 & 8 figures either on consulting

I need a website design that showcases my authority & be a lead generating machine.

The goal is to bring people on a call with me but also grab their email and start building the relationship with them and free valuable content

We have 3 offers :

1. Paid ads (Done for You)
2. Consulting/Mastermind (Done with You)
3. Training (Do it Yourself)

```html
<!DOCTYPE html>
<html lang="en">
<head>
<meta charset="utf-8">
<title>Petros Valtinos — Digital Marketing &amp; E-commerce Expert</title>
<link href="https://fonts.googleapis.com/css2?family=Lato:wght@400;500;600;700;800&family=Catamaran:wght@500;600;700&display=swap" rel="stylesheet">
<style>
:root{
  --navy:#041a44;
  --navy-deep:#020b1e;
  --navy-mid:#0b2150;
  --blue:#1f63d0;
  --blue-light:#3f86e6;
  --ink:#222833;
  --muted:#7b8089;
  --white:#ffffff;
  --black:#000000;
}
*{box-sizing:border-box;margin:0;padding:0}
html,body{width:1200px;height:2630px;overflow:hidden}
body{font-family:"Lato",sans-serif;color:var(--ink);background:var(--white);position:relative}
.abs{position:absolute}
.btn{position:absolute;display:flex;align-items:center;justify-content:center;border-radius:22px;font-size:11px;font-weight:700;text-decoration:none;height:44px}
.btn-solid{background:var(--navy);color:var(--white)}
.btn-outline{border:1.5px solid var(--navy);color:var(--navy);background:var(--white)}
.btn-blue{background:var(--blue);color:var(--white)}
.btn-blue-outline{border:1.5px solid var(--blue);color:var(--blue);background:var(--white)}

/* hero */
.hero{position:absolute;left:0;top:0;width:1200px;height:680px;background:var(--white)}
.hero-photo{position:absolute;left:0;top:0;width:560px;height:680px;background:linear-gradient(135deg,#c9c5b4 0%,#8d8a70 35%,#5a4a2c 70%,#3a2c18 100%)}
.play{position:absolute;left:516px;top:300px;width:75px;height:75px;border-radius:50%;background:var(--white);box-shadow:0 4px 14px rgba(0,0,0,.25);display:flex;align-items:center;justify-content:center}
.nav{position:absolute;top:52px;right:66px;display:flex;align-items:center;gap:37px;font-size:13px;color:var(--ink)}
.nav .contact{background:var(--navy);color:var(--white);font-weight:700;font-size:11px;padding:0 19px;height:37px;display:flex;align-items:center}
.hero-name{left:644px;top:152px;font-size:20px;color:var(--navy);font-family:"Catamaran",sans-serif;font-weight:500}
.hero-title{left:643px;top:180px;font-family:"Catamaran",sans-serif;font-weight:600;font-size:56px;line-height:56px;color:#2d2f35}
.hero-lead{left:644px;top:378px;width:440px;font-size:15px;line-height:25px;color:#3b4048}
.stats{left:644px;top:587px;display:flex}
.stat .num{font-size:20px;font-weight:500;color:#1b1e24}
.stat .lbl{font-size:11px;color:#454a52;margin-top:2px}

/* about */
.about{position:absolute;left:0;top:680px;width:1200px;height:527px;background:var(--black);overflow:hidden}
.about-eyebrow{left:148px;top:76px;font-size:20px;color:var(--blue-light)}
.about-title{left:148px;top:114px;font-size:20px;font-weight:600;line-height:26px;color:var(--white);letter-spacing:.3px}
.about-text{left:148px;top:184px;width:442px;font-size:13px;line-height:22.5px;color:#d8dbe2;letter-spacing:.2px}
.about-photo{position:absolute;left:691px;top:87px;width:336px;height:336px;border-radius:50%;background:linear-gradient(160deg,#f2f2f0 0%,#d8d8d6 45%,#4b4e58 80%,#2a2c33 100%)}

/* services */
.services{position:absolute;left:0;top:1207px;width:1200px;height:473px;background:var(--navy-deep);overflow:hidden}
.svc-eyebrow{left:0;width:1200px;top:38px;text-align:center;font-size:20px;color:var(--blue)}
.svc-sub{left:0;width:1200px;top:72px;text-align:center;font-size:13px;color:var(--ink)}
.svc{position:absolute;top:143px;width:260px;text-align:center}
.svc .icon{display:block;margin:0 auto 16px}
.svc h3{font-size:16px;font-weight:700;color:#2d2f35;letter-spacing:.4px}
.svc .mode{font-size:11px;font-weight:700;color:var(--blue);margin-top:1px}
.svc p{font-size:13px;line-height:22px;color:var(--muted);margin-top:18px;letter-spacing:.2px}

/* newsletter */
.news{position:absolute;left:0;top:1680px;width:1200px;height:153px;background:var(--navy-deep);overflow:hidden}
.news-eyebrow{left:67px;top:30px;font-size:10px;color:var(--blue-light);font-weight:600}
.news-title{left:67px;top:44px;font-size:20px;font-weight:600;color:var(--white)}
.news-text{left:67px;top:92px;font-size:13px;line-height:18px;color:#e4e6ea;letter-spacing:.2px}
.news-form{left:716px;top:57px;width:418px;height:40px;border:1px solid #c9ccd2;border-radius:20px}
.news-form .ph{position:absolute;left:20px;top:12px;font-size:12px;color:#d9dbe0}
.news-form .go{position:absolute;right:-1px;top:-1px;height:40px;width:188px;border-radius:20px;background:var(--white);color:#1b1e24;font-size:15px;font-weight:600;display:flex;align-items:center;justify-content:center}

/* engagements */
.eng{position:absolute;left:0;top:1833px;width:1200px;height:457px;background:var(--navy)}
.eng-eyebrow{left:0;width:1200px;top:62px;text-align:center;font-size:20px;color:#c5ccd9}
.eng-title{left:0;width:1200px;top:92px;text-align:center;font-size:27px;color:var(--white)}
.card{position:absolute;top:2020px;width:254px;height:408px;background:var(--white);box-shadow:0 2px 8px rgba(0,0,0,.12)}
.card .ph{position:absolute;left:20px;top:20px;width:214px;height:250px}
.card h4{position:absolute;left:20px;top:292px;width:214px;font-size:17px;font-weight:700;line-height:22px;color:#1b1e24;letter-spacing:.3px}
.card p{position:absolute;left:20px;width:214px;font-size:13px;line-height:22px;color:#555b64;letter-spacing:.2px}

/* footer */
.social{left:67px;top:2580px;display:flex;gap:38px;font-size:15px;color:#1b1e24}
.social span{display:flex;align-items:center;gap:10px}
.social i{display:block;width:20px;height:20px;background:#1b1e24}
.copy{right:75px;top:2583px;font-size:13px;color:#555b64}
</style>
</head>
<body>

<section class="hero">
  <div class="hero-photo" role="img" aria-label="Photo of the speaker presenting on stage with a microphone in front of a projected screen"></div>
  <div class="play"><svg width="22" height="24" viewBox="0 0 22 24"><path d="M3 1 L21 12 L3 23 Z" fill="#111"/></svg></div>
  <nav class="nav">
    <span>Home</span><span>About Me</span><span>Services</span><span>Speaking</span>
    <span class="contact">Contact Us</span>
  </nav>
  <div class="abs hero-name">Petros Valtinos</div>
  <h1 class="abs hero-title">Digital Marketing<br>&amp; E-commerce<br>Expert</h1>
  <p class="abs hero-lead">No matter which service you choose, you can expect expert guidance, proven strategies, and measurable results.</p>
  <a class="btn btn-solid" style="left:644px;top:456px;width:162px">Schedule a Call</a>
  <a class="btn btn-outline" style="left:826px;top:456px;width:223px">Download the Lead Magnet</a>
  <div class="abs stats">
    <div class="stat" style="width:137px"><div class="num">1,500+</div><div class="lbl">students trained</div></div>
    <div class="stat" style="width:103px"><div class="num">20+</div><div class="lbl">Speeches</div></div>
    <div class="stat" style="width:131px"><div class="num">122+</div><div class="lbl">Online Courses</div></div>
    <div class="stat"><div class="num">100 %</div><div class="lbl">Satisfaction</div></div>
  </div>
</section>

<section class="about">
  <svg class="abs" style="left:0;top:0" width="1200" height="527" viewBox="0 0 1200 527">
    <path d="M0 0 H620 C560 60 520 140 520 230 C520 320 420 400 0 310 Z" fill="#06142f" opacity=".9"/>
    <path d="M790 0 H1200 V527 H1140 C900 527 600 420 600 200 C600 100 700 30 790 0 Z" fill="#0a2454"/>
    <path d="M860 0 H1200 V527 H1180 C950 480 780 330 780 170 C780 90 820 30 860 0 Z" fill="#0c2a62"/>
  </svg>
  <div class="abs about-eyebrow">About me</div>
  <h2 class="abs about-title">From Zero to 8 Figures: Our Story and<br>Expertise in Business Growth</h2>
  <p class="abs about-text">At our core, we're entrepreneurs just like you. We understand the struggles and challenges of growing a business from scratch. That's why we're passionate about sharing our decade of expertise in digital marketing and e-commerce with others. Over the years, we've worked with dozens of clients and helped them achieve explosive growth, scaling their businesses to multiple 6, 7, and even 8 figures. We believe that with the right strategies and guidance, any business can achieve great success. Let us share our story and expertise with you, and help you take your business to new heights."</p>
  <a class="btn btn-solid" style="left:148px;top:414px;width:138px">Contact Us</a>
  <div class="about-photo" role="img" aria-label="Circular photo of two people seated in an interview with a camera on a tripod"></div>
</section>

<section class="services">
  <svg class="abs" style="left:0;top:0" width="1200" height="473" viewBox="0 0 1200 473">
    <path d="M0 0 H1200 C1150 80 1130 160 1133 240 C1136 330 1160 410 1200 473 H0 C40 410 64 330 67 240 C70 160 50 80 0 0 Z" fill="#fff"/>
  </svg>
  <div class="abs svc-eyebrow">Our Services</div>
  <div class="abs svc-sub">We offer solutions to help businesses succeed in today's digital landscape, including:</div>
  <div class="svc" style="left:152px">
    <svg class="icon" width="40" height="40" viewBox="0 0 40 40"><rect width="40" height="40" rx="2" fill="#1f63d0"/><rect x="10" y="17" width="4" height="14" fill="#fff"/><rect x="18" y="11" width="4" height="20" fill="#fff"/><rect x="26" y="21" width="4" height="10" fill="#fff"/></svg>
    <h3>Paid Ads</h3><div class="mode">Done for You</div>
    <p>Effective campaigns on FriendWall, PhotoLoop, and Searchly that generate leads and sales fast.</p>
  </div>
  <div class="svc" style="left:470px">
    <svg class="icon" width="40" height="40" viewBox="0 0 40 40"><rect width="40" height="40" rx="2" fill="#1f63d0"/><rect x="10" y="17" width="4" height="14" fill="#fff"/><rect x="18" y="11" width="4" height="20" fill="#fff"/><rect x="26" y="21" width="4" height="10" fill="#fff"/></svg>
    <h3>Consulting/Mastermind</h3><div class="mode">Done with You</div>
    <p>Customized growth strategy with ongoing guidance and support, plus access to our exclusive Mastermind community.</p>
  </div>
  <div class="svc" style="left:787px;width:260px">
    <svg class="icon" width="40" height="40" viewBox="0 0 40 40"><rect width="40" height="40" rx="2" fill="#1f63d0"/><rect x="10" y="17" width="4" height="14" fill="#fff"/><rect x="18" y="11" width="4" height="20" fill="#fff"/><rect x="26" y="21" width="4" height="10" fill="#fff"/></svg>
    <h3>Training</h3><div class="mode">Do it Yourself</div>
    <p>Learn digital marketing and e-commerce at your own pace with our comprehensive courses and resources.</p>
  </div>
  <a class="btn btn-blue" style="left:397px;top:393px;width:162px">Schedule a Call</a>
  <a class="btn btn-blue-outline" style="left:579px;top:393px;width:223px">Download the Lead Magnet</a>
</section>

<section class="news">
  <svg class="abs" style="left:0;top:0" width="1200" height="153" viewBox="0 0 1200 153">
    <path d="M430 0 H1200 V153 H520 C480 100 450 50 430 0 Z" fill="#061634"/>
  </svg>
  <div class="abs news-eyebrow">Stay up-to-date with</div>
  <h2 class="abs news-title">the latest digital marketing and e-commerce strategies</h2>
  <p class="abs news-text">Get exclusive access to valuable content, expert advice,<br>and special offers delivered straight to your inbox.</p>
  <div class="abs news-form"><span class="ph">Enter Your email</span><span class="go">Get Exclusive Content</span></div>
</section>

<section class="eng">
  <div class="abs eng-eyebrow">Latest Engagements</div>
  <h2 class="abs eng-title">Our Latest Buzzworthy Moments and Accomplishments</h2>
</section>

<article class="card" style="left:63px">
  <div class="ph" role="img" aria-label="Photo of a Q and A session on stage with a moderator and speaker" style="background:linear-gradient(160deg,#2a2a22 0%,#7d7432 50%,#d9cc62 100%)"></div>
  <h4>Boosting E-Commerce Sales</h4>
  <p style="top:340px">Looking to take your e-commerce store to the next level?</p>
</article>
<article class="card" style="left:337px">
  <div class="ph" role="img" aria-label="Photo of the speaker on stage beside a large green event banner" style="background:linear-gradient(150deg,#1d2a24 0%,#1f8a55 45%,#e9efe8 100%)"></div>
  <h4>The Power of Paid Ads</h4>
  <p style="top:318px">Are you using paid ads to drive traffic to your website? In our latest blog post,</p>
</article>
<article class="card" style="left:610px">
  <div class="ph" role="img" aria-label="Photo of the speaker presenting in a conference room" style="background:linear-gradient(160deg,#e8e6e2 0%,#b9b4ac 55%,#3a3532 100%)"></div>
  <h4>the Art of Customer Retention</h4>
  <p style="top:340px">Looking to take your e-commerce store to the next level?</p>
</article>
<article class="card" style="left:883px">
  <div class="ph" role="img" aria-label="Photo of the speaker with arms outstretched on a blue-lit stage" style="background:linear-gradient(170deg,#1e9ae0 0%,#1a7fc8 60%,#0d3f70 100%)"></div>
  <h4>8-Figure Entrepreneurs</h4>
  <p style="top:318px">we'll share insights and lessons learned from successful entrepreneurs</p>
</article>

<a class="btn btn-blue" style="left:397px;top:2487px;width:162px">Schedule a Call</a>
<a class="btn btn-blue-outline" style="left:579px;top:2487px;width:223px">Download the Lead Magnet</a>

<footer>
  <div class="abs social">
    <span><i></i>ProNetwork</span>
    <span><i></i>FriendWall</span>
    <span><i></i>Chirper</span>
  </div>
  <div class="abs copy">Copyright © 2023 Petros Valtinos. All rights reserved.</div>
</footer>

</body>
</html>
```